Presentation Folder Art

We need to update our existing presentation folder and need to integrate the various aspects of the testing we do. This isn't easy as our testing is diverse, as seen by the various icon categories we have. We will keep the icons on the inside cover so we don't have an opinion either way if they are kept on the cover or not. A copy of our current folder art is attached (Cover-Diecut-Outlines). I have also uploaded one of our current brochures to see the type of style we're happy with.

Target Market(s)

product manufacturers, importers ranging from commercial to military

Requirements
Must have
• Should integrate our corporate colors of orange and dark blue

```html
<!DOCTYPE html>
<html lang="en">
<head>
<meta charset="utf-8">
<title>Presentation Folder – Global Testing and Approvals</title>
<link rel="stylesheet" href="https://fonts.googleapis.com/css2?family=Open+Sans:ital,wght@0,400;0,600;0,700;1,700&display=swap">
<style>
  :root {
    --stage: #c9cacc;
    --blue: #1a6fb8;
    --blue-deep: #0f4f8e;
    --blue-light: #3f8fd0;
    --orange: #f08a1c;
    --white: #ffffff;
    --inside-grey: #a9abae;
    --services-text: #d7e6f3;
  }
  * { box-sizing: border-box; margin: 0; padding: 0; }
  html, body {
    width: 1200px; height: 675px; overflow: hidden;
    background: var(--stage);
    font-family: "Open Sans", Arial, sans-serif;
  }
  .spread {
    position: absolute; left: 160px; top: 37px;
    display: flex; gap: 40px;
  }
  .panel {
    position: relative; width: 420px; height: 600px; overflow: hidden;
    box-shadow: 0 10px 24px rgba(0, 0, 0, 0.18);
  }

  /* Front cover */
  .cover {
    background: linear-gradient(180deg, var(--blue-light) 0%, var(--blue) 45%, var(--blue-deep) 100%);
  }
  .cover__imagery { position: absolute; inset: 0; width: 420px; height: 600px; }
  .brand {
    position: absolute; right: 0; top: 0;
    width: 150px; height: 92px;
    background: var(--white);
    border-bottom-left-radius: 14px;
    clip-path: polygon(14% 0, 100% 0, 100% 100%, 0 100%, 0 22%);
    display: flex; flex-direction: column; align-items: flex-end; justify-content: center;
    padding-right: 16px;
  }
  .brand__row { display: flex; align-items: center; gap: 6px; }
  .brand__mark { width: 12px; height: 12px; background: var(--blue-deep); }
  .brand__name { font-weight: 700; font-size: 19px; color: var(--blue-deep); letter-spacing: 0.5px; }
  .brand__sub { font-size: 6px; color: var(--blue-deep); letter-spacing: 1.5px; margin-top: 2px; }
  .tagline {
    position: absolute; left: 262px; top: 432px;
    font-weight: 700; font-style: italic; font-size: 14px; line-height: 1.3;
    text-transform: uppercase;
  }
  .tagline__lead { color: var(--orange); display: block; }
  .tagline__rest { color: var(--white); display: block; }
  .services {
    position: absolute; left: 22px; bottom: 36px;
    display: flex; gap: 18px; list-style: none;
    font-size: 7.5px; letter-spacing: 0.8px; color: var(--services-text); text-transform: uppercase;
  }
  .services li { display: flex; align-items: center; gap: 4px; }
  .services li::before { content: ""; width: 5px; height: 5px; background: var(--orange); }

  /* Inside panel with pocket */
  .inside { background: linear-gradient(180deg, #b5b7ba, var(--inside-grey)); }
  .pocket {
    position: absolute; left: 0; right: 0; bottom: 0; height: 200px;
    background: linear-gradient(180deg, var(--blue) 0%, var(--blue-deep) 100%);
    box-shadow: 0 -3px 8px rgba(0, 0, 0, 0.15);
  }
  .categories {
    position: absolute; left: 50%; top: 34px; transform: translateX(-50%);
    display: flex; gap: 22px; list-style: none;
  }
  .category { display: flex; flex-direction: column; align-items: center; gap: 6px; }
  .category__icon {
    width: 40px; height: 40px; border-radius: 50%;
    background: var(--orange); border: 2px solid var(--white);
    display: flex; align-items: center; justify-content: center;
  }
  .category__label { font-size: 7px; letter-spacing: 0.8px; color: var(--white); text-transform: uppercase; }
</style>
</head>
<body>
  <main class="spread">
    <section class="panel cover" aria-label="Front cover">
      <svg class="cover__imagery" viewBox="0 0 420 600" aria-hidden="false">
        <defs>
          <linearGradient id="sky" x1="0" y1="0" x2="0.4" y2="1">
            <stop offset="0" stop-color="#d3dde7"/>
            <stop offset="0.5" stop-color="#a5b8ca"/>
            <stop offset="1" stop-color="#7f97ad"/>
          </linearGradient>
          <radialGradient id="skyShade" cx="0.5" cy="0.5" r="0.45">
            <stop offset="0" stop-color="#4a5766" stop-opacity="0.55"/>
            <stop offset="1" stop-color="#4a5766" stop-opacity="0"/>
          </radialGradient>
          <linearGradient id="sea" x1="0" y1="0" x2="0" y2="1">
            <stop offset="0" stop-color="#9fbdd2"/>
            <stop offset="0.35" stop-color="#5d8cad"/>
            <stop offset="0.75" stop-color="#2f6186"/>
            <stop offset="1" stop-color="#2a5677"/>
          </linearGradient>
          <radialGradient id="seaShade" cx="0.55" cy="0.55" r="0.5">
            <stop offset="0" stop-color="#1f2f3d" stop-opacity="0.5"/>
            <stop offset="1" stop-color="#1f2f3d" stop-opacity="0"/>
          </radialGradient>
          <linearGradient id="ground" x1="0" y1="0" x2="0" y2="1">
            <stop offset="0" stop-color="#c4c8cc"/>
            <stop offset="0.3" stop-color="#6b7076"/>
            <stop offset="0.65" stop-color="#2c3034"/>
            <stop offset="1" stop-color="#a3a7ab"/>
          </linearGradient>
          <radialGradient id="groundShade" cx="0.5" cy="0.5" r="0.5">
            <stop offset="0" stop-color="#16181a" stop-opacity="0.55"/>
            <stop offset="1" stop-color="#16181a" stop-opacity="0"/>
          </radialGradient>
        </defs>

        <g role="img" aria-label="Photo: fighter jet flying above clouds">
          <path d="M118,-10 H300 L318,60 V190 L222,262 L120,220 L100,160 V40 Z"
                fill="url(#sky)" stroke="url(#sky)" stroke-width="18" stroke-linejoin="round"/>
          <ellipse cx="210" cy="130" rx="90" ry="80" fill="url(#skyShade)"/>
        </g>

        <g role="img" aria-label="Photo: submarine cutting through the sea">
          <path d="M300,110 H430 V400 H258 V172 Z"
                fill="url(#sea)" stroke="url(#sea)" stroke-width="18" stroke-linejoin="round"/>
          <ellipse cx="345" cy="240" rx="70" ry="90" fill="url(#seaShade)"/>
        </g>

        <g role="img" aria-label="Photo: armoured military vehicle on a road">
          <path d="M118,240 H198 L236,276 V530 H54 V300 Z"
                fill="url(#ground)" stroke="url(#ground)" stroke-width="18" stroke-linejoin="round"/>
          <ellipse cx="145" cy="390" rx="95" ry="100" fill="url(#groundShade)"/>
        </g>
      </svg>

      <div class="brand">
        <div class="brand__row"><span class="brand__mark"></span><span class="brand__name">VERITEK</span></div>
        <span class="brand__sub">LABORATORIES</span>
      </div>
      <h1 class="tagline"><span class="tagline__lead">Global Testing</span><span class="tagline__rest">and Approvals</span></h1>
      <ul class="services">
        <li>EMC &amp; Telecoms</li>
        <li>Safety</li>
        <li>Energy Efficiency</li>
        <li>Environmental</li>
      </ul>
    </section>

    <section class="panel inside" aria-label="Inside pocket">
      <div class="pocket">
        <ul class="categories">
          <li class="category">
            <span class="category__icon">
              <svg width="20" height="20" viewBox="0 0 20 20"><circle cx="10" cy="10" r="7" fill="none" stroke="#fff" stroke-width="2"/><path d="M6 12 Q10 4 14 8" fill="none" stroke="#fff" stroke-width="2"/></svg>
            </span>
            <span class="category__label">Environmental</span>
          </li>
          <li class="category">
            <span class="category__icon">
              <svg width="20" height="20" viewBox="0 0 20 20"><path d="M10 3 L18 17 H2 Z" fill="none" stroke="#fff" stroke-width="2" stroke-linejoin="round"/></svg>
            </span>
            <span class="category__label">Approvals</span>
          </li>
          <li class="category">
            <span class="category__icon">
              <svg width="20" height="20" viewBox="0 0 20 20"><circle cx="10" cy="10" r="2.5" fill="#fff"/><path d="M6 6 A6 6 0 0 0 6 14 M14 6 A6 6 0 0 1 14 14" fill="none" stroke="#fff" stroke-width="2"/></svg>
            </span>
            <span class="category__label">Alarms</span>
          </li>
          <li class="category">
            <span class="category__icon">
              <svg width="20" height="20" viewBox="0 0 20 20"><rect x="5" y="5" width="10" height="10" rx="2" fill="#fff"/></svg>
            </span>
            <span class="category__label">Toys</span>
          </li>
        </ul>
      </div>
    </section>
  </main>
</body>
</html>
```